We manage actors careers and book them liaising and promoting their profiles internationally through Casting Directors, Producers, Directors, Publicists etc. We need clearly visable contact details but with a design that reflects our status and creativity of TV, Feature Film industry. Our logo is attached and needs to relate and our website is www.brovanelpartners.example
No flame designs please but please incorporate logo colours.

Target Market(s)

Clients

Industry/Entity Type

Film Production

Contact Information for Business Card

Director Danielle Pacrow
Suite F, Building 7, Wren Lot Studios, Tallis Reach, Sydney, NSW 2094

Font styles to use
Sans Serif

Colors
ec1f27

Requirements
Nice to have
• Colours should relate to logo attached and type can relate again to type in the logo design.
Should not have
• No Flames designs and best to be not too obvious with the film designs eiither. Needs to be more creative and modern

```html
<!DOCTYPE html>
<html lang="en">
<head>
<meta charset="utf-8">
<title>Brovanel Partners – Business Card</title>
<link rel="stylesheet" href="https://fonts.googleapis.com/css2?family=Limelight&display=swap">
<style>
  :root {
    --page: #ffffff;
    --red-deep: #940c10;
    --red-mid: #c11a20;
    --red-glow: #ec1f27;
    --silver: #e4e4e4;
    --ink-light: #f4f1f1;
  }
  * { margin: 0; padding: 0; box-sizing: border-box; }
  html, body {
    width: 1200px;
    height: 1000px;
    overflow: hidden;
    background: var(--page);
  }
  .canvas {
    position: relative;
    width: 1200px;
    height: 1000px;
    font-family: "Limelight", sans-serif;
  }
  .card {
    position: absolute;
    left: 193px;
    width: 780px;
    height: 456px;
    background:
      radial-gradient(ellipse 78% 100% at 50% 15%,
        var(--red-glow) 0%,
        var(--red-mid) 48%,
        var(--red-deep) 82%);
    overflow: hidden;
  }
  .card--front { top: 35px; }
  .card--back { top: 500px; }

  .brand-name {
    position: absolute;
    left: 0;
    right: 0;
    top: 186px;
    text-align: center;
    font-size: 64px;
    line-height: 1;
    color: var(--silver);
    letter-spacing: 1px;
  }

  .contact-name {
    position: absolute;
    left: 0;
    right: 0;
    top: 122px;
    text-align: center;
    font-size: 46px;
    line-height: 1;
    color: var(--ink-light);
    letter-spacing: 0.5px;
  }
  .contact-address {
    position: absolute;
    left: 0;
    right: 0;
    top: 236px;
    text-align: center;
    font-size: 26px;
    line-height: 40px;
    color: var(--ink-light);
    font-style: normal;
  }
</style>
</head>
<body>
  <main class="canvas">
    <section class="card card--front" aria-label="Card front">
      <h1 class="brand-name">Brovanel Partners</h1>
    </section>

    <section class="card card--back" aria-label="Card back">
      <p class="contact-name">Director Danielle Pacrow</p>
      <address class="contact-address">
        Suite F, Building 7,<br>
        Wren Lot Studios, Tallis Reach,<br>
        Sydney, NSW 2094
      </address>
    </section>
  </main>
</body>
</html>
```